Software company needs a great powerpoint template

We need a powerpoint template for our growing company. Our software helps hospitals achieve quality via automating tedius manual tasks, performing them better, faster and easier than a person can. See our logo below and check out our website at qrn-medivault.com for more ideas/informaton. We will use this template for sales presentations, trade show demonstrations and partnership proposals.

Target Market(s)

Hospital managers & directors

Industry/Entity Type

Hospital

Contact Information for Business Card

name, title, office telephone, cell phone, email and website

Font styles to use
Sans Serif

Colors
2f74b3
33b8a4

Requirements
Must have
• use blues and greens, san serif fonts
Nice to have
• modern feel yet still somewhat converative

```html
<!DOCTYPE html>
<html lang="en">
<head>
<meta charset="utf-8">
<title>QRN Presentation Template</title>
<link href="https://fonts.googleapis.com/css2?family=Fira+Sans:wght@300;400;600;700&family=Fira+Sans+Condensed:wght@800&display=swap" rel="stylesheet">
<style>
  :root{
    --blue:#2f74b3;
    --title-blue:#1f5fa8;
    --navy:#1b3a63;
    --slate:#3f5068;
    --sky:#a9cbea;
    --mid-blue:#5b9bd5;
    --teal:#33b8a4;
    --teal-dark:#2e93a8;
    --pale:#e3eef8;
    --grey:#6b7480;
    --line:#9fd6cc;
    --page:#ffffff;
  }
  *{box-sizing:border-box;margin:0;padding:0}
  html,body{width:1200px;height:1200px;overflow:hidden;background:var(--page)}
  body{position:relative;font-family:"Fira Sans",sans-serif;color:var(--grey)}

  .slide{position:absolute;width:325px;height:183px;background:#fff;border:1px solid #c9ccd1;overflow:hidden}
  .slide--hero{left:260px;top:50px;transform-origin:0 0;transform:scale(2.092)}
  .slide--title-thumb{left:76px;top:505px}
  .slide--layout{left:442px;top:505px}
  .slide--colors{left:808px;top:505px}
  .slide--contents{left:76px;top:736px}
  .slide--points{left:442px;top:736px}
  .slide--image-right{left:808px;top:736px}
  .slide--data{left:262px;top:967px}
  .slide--thanks{left:628px;top:967px;border:none}

  .headline{position:absolute;left:12px;top:7px;font-weight:700;font-size:12.5px;color:var(--title-blue);white-space:nowrap}
  .subhead{position:absolute;left:12px;top:23px;font-weight:300;font-size:5.5px;color:var(--sky);letter-spacing:.2px}
  .brand{position:absolute;right:8px;top:6px;display:flex;align-items:center;gap:2px;font-weight:700;font-size:11px;color:var(--title-blue)}
  .brand__dot{width:5px;height:5px;border-radius:50%;background:var(--teal)}
  .footer-line{position:absolute;left:0;right:0;bottom:7px;height:1px;background:var(--line)}
  .page-num{position:absolute;bottom:1px;left:0;right:0;text-align:center;font-size:3px;color:#aaa}
  .footnote{position:absolute;left:12px;bottom:11px;font-size:2.8px;line-height:3.6px;color:#999}

  .photo{position:absolute}

  /* title slide */
  .title-bg{left:0;top:0;width:100%;height:100%;background:linear-gradient(100deg,#f4f8fc 0%,#e6eff7 40%,#bfd4e6 70%,#8aa6bf 100%)}
  .title-main{position:absolute;left:12px;top:68px;font-weight:700;font-size:19.5px;color:var(--title-blue);white-space:nowrap}
  .title-sub{position:absolute;left:12px;top:97px;font-weight:300;font-size:6.5px;color:#444}
  .title-date{position:absolute;left:12px;top:152px;font-weight:300;font-size:7px;color:#444}
  .title-brand{position:absolute;right:12px;bottom:16px;display:flex;align-items:center;gap:4px;font-weight:700;font-size:28px;color:var(--title-blue)}
  .title-brand .brand__dot{width:11px;height:11px}

  .bullets{position:absolute;list-style:none;font-weight:300;color:#555}
  .bullets li{position:relative;padding-left:6px}
  .bullets li::before{content:"";position:absolute;left:0;width:2px;height:2px;border-radius:50%;background:var(--teal)}

  .bullets--levels{left:14px;top:75px;font-size:4.2px;line-height:7.5px}
  .bullets--levels li::before{top:2.8px}
  .bullets--levels .l2{margin-left:6px}
  .bullets--levels .l3{margin-left:12px}

  .swatches{position:absolute;left:12px;top:85px;display:flex;gap:3px}
  .swatches span{width:28px;height:30px;border:1px solid #ddd}

  .contents{position:absolute;left:0;top:52px;width:100%}
  .contents li{list-style:none;height:17px;margin-bottom:2.5px;padding-left:26px;line-height:17px;font-size:6px;color:#555;background:linear-gradient(90deg,#d6e6f5 0%,#e8f1fa 70%,rgba(255,255,255,0) 100%)}

  .bullets--body{font-size:8px;line-height:11px}
  .bullets--body li{margin-bottom:4px}
  .bullets--body li::before{top:4.5px;width:2.5px;height:2.5px}
  .bullets--points{left:38px;top:60px;width:200px}
  .bullets--right{left:192px;top:67px;width:120px;font-size:7.5px;line-height:10.5px}

  .data-text{position:absolute;left:62px;top:45px;width:64px;height:119px;background:linear-gradient(90deg,#f4f8fc,#d5e6f5);padding:6px 3px 0 6px}
  .bullets--data{position:static;font-size:5px;line-height:6px}
  .bullets--data li{margin-bottom:4px}
  .bullets--data li::before{top:2px}
  .chart{position:absolute;left:130px;top:45px;width:143px;height:119px;border:1px solid #cfdbe6}
  .chart__head{background:var(--teal);color:#fff;font-weight:700;font-size:4.5px;padding:2px 3px;height:9px}
  .chart__units{display:flex;justify-content:space-between;font-size:3.8px;padding:2px 3px;color:#999;height:20px}
  .chart__units b{font-weight:400;color:var(--teal)}
  .chart__row{display:flex;align-items:center;height:16px;margin:0 3px 3px;background:linear-gradient(90deg,#fff 20%,#eaf2fa 60%,#fff);font-size:4.5px}
  .chart__label{width:40px;text-align:right;padding-right:3px}
  .chart__bar{height:9px}
  .chart__val{margin-left:auto;padding-right:14px;font-size:3.8px}

  .thanks-bg{left:0;top:0;width:100%;height:100%;background:linear-gradient(160deg,#c3d5e6 0%,#7fa0c4 45%,#5f86b3 70%,#8fb1d0 100%)}
  .thanks-band{position:absolute;left:0;right:0;top:99px;bottom:0;background:linear-gradient(180deg,#33b8a4 0%,#3aa99a 60%,#5fb8ae 100%)}
  .thanks-title{position:absolute;left:0;right:0;top:97px;text-align:center;font-family:"Fira Sans Condensed",sans-serif;font-weight:800;font-size:29px;letter-spacing:.5px;color:#fff}
  .thanks-contact{position:absolute;left:0;right:0;top:134px;display:flex;justify-content:center;gap:7px;font-weight:700;font-size:5px;color:#fff}
  .thanks-contact span{display:flex;align-items:center;gap:2px}
  .thanks-brand{position:absolute;left:0;right:0;top:150px;display:flex;justify-content:center;align-items:center;gap:3px;font-weight:700;font-size:18px;color:var(--title-blue)}
  .thanks-brand .brand__dot{width:7px;height:7px}
</style>
</head>
<body>

<!-- hero title slide -->
<section class="slide slide--hero">
  <div class="photo title-bg" role="img" aria-label="Photo of a scientist in a lab coat holding a tablet in a laboratory, soft blue tones"></div>
  <h1 class="title-main">Title of the Document</h1>
  <p class="title-sub">SUBTITLE OF THE DOCUMENT</p>
  <p class="title-date">February 2017, NY</p>
  <div class="title-brand"><span class="brand__dot"></span>QRN</div>
</section>

<section class="slide slide--title-thumb">
  <div class="photo title-bg" role="img" aria-label="Photo of a scientist in a lab coat holding a tablet in a laboratory, soft blue tones"></div>
  <h1 class="title-main">Title of the Document</h1>
  <p class="title-sub">SUBTITLE OF THE DOCUMENT</p>
  <p class="title-date">February 2017, NY</p>
  <div class="title-brand"><span class="brand__dot"></span>QRN</div>
</section>

<section class="slide slide--layout">
  <h2 class="headline">LAYOUT: Headline and content</h2>
  <p class="subhead">SUBTITLE</p>
  <div class="brand"><span class="brand__dot"></span>QRN</div>
  <ul class="bullets bullets--levels">
    <li>First level bullet</li>
    <li class="l2">Second level bullet</li>
    <li class="l3">Third level bullet</li>
  </ul>
  <p class="footnote">* Footnote text here<br>Source: add source here</p>
  <div class="footer-line"></div><span class="page-num">2</span>
</section>

<section class="slide slide--colors">
  <h2 class="headline">Color harmony</h2>
  <p class="subhead">SUBTITLE</p>
  <div class="brand"><span class="brand__dot"></span>QRN</div>
  <div class="swatches">
    <span style="background:#fff"></span>
    <span style="background:#000"></span>
    <span style="background:#33b0a0"></span>
    <span style="background:var(--slate)"></span>
    <span style="background:var(--sky)"></span>
    <span style="background:var(--mid-blue)"></span>
    <span style="background:var(--blue)"></span>
    <span style="background:var(--navy)"></span>
    <span style="background:var(--teal-dark)"></span>
    <span style="background:var(--teal)"></span>
  </div>
  <div class="footer-line"></div>
</section>

<section class="slide slide--contents">
  <h2 class="headline">Contents slide</h2>
  <p class="subhead">SUBTITLE</p>
  <div class="brand"><span class="brand__dot"></span>QRN</div>
  <ul class="contents">
    <li>Executive summary</li>
    <li>Enabling technologies</li>
    <li>Growth Impact on public sector</li>
    <li>Risk mitigation</li>
    <li>Next steps</li>
    <li>Appendix</li>
  </ul>
  <div class="footer-line"></div><span class="page-num">4</span>
</section>

<section class="slide slide--points">
  <div class="photo" style="right:0;top:0;width:115px;height:183px;background:linear-gradient(90deg,rgba(255,255,255,1) 0%,#e9eef3 35%,#c7d6e4 70%,#5d9fd8 100%)" role="img" aria-label="Photo of a masked lab researcher in blue gloves holding a petri dish"></div>
  <h2 class="headline">LAYOUT: 3 points text</h2>
  <p class="subhead">SUBTITLE</p>
  <div class="brand"><span class="brand__dot"></span>QRN</div>
  <ul class="bullets bullets--body bullets--points">
    <li>Lorem ipsum dolor sit amet, consectetur adipiscing elit</li>
    <li>Suspendisse lacinia ex dolor, nec facilisis magna semper non</li>
    <li>Nam cursus diam ut fringilla dapibus. Nulla maximus finibus libero.</li>
  </ul>
  <p class="footnote">* Footnote text here<br>Source: add source here</p>
  <div class="footer-line"></div><span class="page-num">5</span>
</section>

<section class="slide slide--image-right" style="height:186px">
  <div class="photo" style="left:0;top:28px;width:190px;height:158px;background:linear-gradient(90deg,#b9cde0 0%,#dbe6f0 55%,rgba(255,255,255,1) 100%)" role="img" aria-label="Photo of two lab researchers in safety glasses examining a flask"></div>
  <h2 class="headline">LAYOUT: Image with text on right</h2>
  <p class="subhead">SUBTITLE</p>
  <div class="brand"><span class="brand__dot"></span>QRN</div>
  <ul class="bullets bullets--body bullets--right">
    <li>Lorem ipsum dolor sit amet, consectetur adipiscing elit</li>
    <li>Suspendisse lacinia ex dolor, nec facilisis magna semper non</li>
    <li>Nam cursus diam ut fringilla dapibus. Nulla maximus finibus libero.</li>
  </ul>
  <div class="footer-line"></div><span class="page-num">6</span>
</section>

<section class="slide slide--data">
  <h2 class="headline">LAYOUT: Data with Text on left</h2>
  <p class="subhead">SUBTITLE</p>
  <div class="brand"><span class="brand__dot"></span>QRN</div>
  <div class="data-text">
    <ul class="bullets bullets--data">
      <li>Lorem ipsum dolor sit amet, consectetur adipiscing elit</li>
      <li>Suspendisse lacinia ex dolor, nec facilisis magna semper non</li>
      <li>Nam cursus diam ut fringilla dapibus. Nulla maximus finibus libero.</li>
    </ul>
  </div>
  <div class="chart">
    <div class="chart__head">Net Sales 2016</div>
    <div class="chart__units"><span>EUR mn</span><b>Growth,<br>%</b></div>
    <div class="chart__row"><span class="chart__label">Company A</span><span class="chart__bar" style="width:42px;background:var(--title-blue)"></span><span class="chart__val">xx</span></div>
    <div class="chart__row"><span class="chart__label">Company B</span><span class="chart__bar" style="width:31px;background:var(--sky)"></span><span class="chart__val">xx</span></div>
    <div class="chart__row"><span class="chart__label">Company C</span><span class="chart__bar" style="width:13px;background:var(--sky)"></span><span class="chart__val">xx</span></div>
    <div class="chart__row"><span class="chart__label">Company D</span><span class="chart__bar" style="width:9px;background:var(--sky)"></span><span class="chart__val">xx</span></div>
  </div>
  <p class="footnote">* Footnote text here<br>Source: add source here</p>
  <div class="footer-line"></div><span class="page-num">7</span>
</section>

<section class="slide slide--thanks">
  <div class="photo thanks-bg" role="img" aria-label="Photo of medical staff with a translucent heart-rate monitor overlay in blue"></div>
  <div class="thanks-band"></div>
  <h2 class="thanks-title">THANK YOU</h2>
  <div class="thanks-contact">
    <span><svg width="6" height="5" viewBox="0 0 12 10"><path d="M1 3C1 1 3 0 6 0s5 1 5 3L9 4 8 2H4L3 4zM2 5h8v5H2z" fill="#fff"/></svg>555-010-0142</span>
    <span><svg width="6" height="5" viewBox="0 0 12 9"><rect x="0" y="0" width="12" height="9" fill="#fff"/><path d="M0 0l6 5 6-5" stroke="#33b8a4" fill="none"/></svg>info@qrn-medivault.com</span>
    <span><svg width="6" height="5" viewBox="0 0 12 9"><rect x="0" y="0" width="12" height="9" fill="#fff"/><path d="M0 0l6 5 6-5" stroke="#33b8a4" fill="none"/></svg>http://www.qrn-medivault.com</span>
  </div>
  <div class="thanks-brand"><span class="brand__dot"></span>QRN</div>
</section>

</body>
</html>
```